依頼詳細
・B4、両面カラー
・明るく楽しい雰囲気、お客様に安心感・信頼が伝わるようなイメージ。
(安っぽくならないようにご注意ください。お願いします。
・画像使用の場合は、制作者様側でご用意ください。
・オプションの習いごと3つの詳細を掲載ください。
(名前・ロゴ・詳細・写真はご依頼確定後にお渡しいたします。)
・来年度募集「キャンペーン」をもとに説明会に参加、スクール入会したくなるようなチラシにしていただきたいです。
記載項目
社名/電話番号/URL/メールアドレス/住所/キャッチコピー/料金/学童のポイント/学童内容/習い紹介//キャンペーン情報/イベント&説明会情報/

※その他詳細は添付ファイルPDFをご確認下さい。
サイズ
B4
ページ数
両面
希望イメージ
シンプル 複雑
単色 カラフル
暗い 明るい
日常 高級
遊び心 厳粛
未来的 伝統的
女性的 男性的
希望する色
水色系、緑系、黄・オレンジ系
納品ファイル
• 高解像度JPG (.jpg)
• イラストレーター形式 (.ai)
• PNG形式 (.png)
補足説明
詳細内容は指示書に記載しました。恐れ入りますがご確認ください。
その他弊社HPも参考にご確認ください。https://www.hoshizora-gakudo.jp/
■ 選んだ理由

イラストや図形を使って、可愛らしくもありながら信頼や安心感も伝わるデザインであり、今回私たちが求めるデザインに最も近いと思いました。お客様に伝えたい情報や、スクールの様子などが最も伝わる構成でもあり、当選させていただきました。
また、こちらからの加筆修正に対するレスポンスの早さと丁寧な対応を通じて、デザイナーさんの誠実さを感じられたのも当選理由の一つです。

■ 提案者全員のお礼・コメント

この度はコンペにご参加・ご提出していただき、誠にありがとうございました。
デザイナー様の提案内容と共に、ご提出いただいた案全て、慎重に拝見させていただきました。どの案もとても素晴らしく、一つに絞るのがとても大変でした。

今回ご提出いただいたデザイナーの皆さまに改めて心より感謝申し上げます。
また、コンペを開催した際にはぜひ提案いただけますと幸いです。今後とも、どうぞ宜しくお願い致します。

```html
<!DOCTYPE html>
<html lang="ja">
<head>
<meta charset="utf-8">
<title>HOSHIZORAキッズ 2024年度 学童入会員募集</title>
<link rel="stylesheet" href="https://fonts.googleapis.com/css2?family=M+PLUS+Rounded+1c:wght@500;800;900&display=swap">
<style>
:root{
  --green:#8cc63f;
  --green-dark:#3f9a36;
  --orange:#f39800;
  --orange-dark:#e06a00;
  --yellow:#ffe600;
  --ink:#333333;
  --white:#ffffff;
  --photo:#c9d3cf;
  --accent-soft:#c4e08a;
}
*{box-sizing:border-box;margin:0;padding:0}
html,body{width:849px;height:1200px;overflow:hidden}
body{font-family:"M PLUS Rounded 1c",sans-serif;color:var(--ink);background:var(--green)}
.flyer{position:relative;width:849px;height:1200px;background:var(--green);overflow:hidden}
.abs{position:absolute}

.masthead{left:0;top:0;width:849px;height:150px;background:var(--white);border-radius:0 0 60px 60px;text-align:center}
.tagline{position:absolute;top:20px;width:100%;font-size:14px;font-weight:800;color:var(--green-dark);letter-spacing:.1em}
.brand{position:absolute;top:48px;width:100%;display:flex;justify-content:center;align-items:center;gap:12px}
.brand-dot{width:26px;height:26px;border-radius:50%;background:var(--orange)}
.brand-name{font-size:52px;font-weight:900;color:var(--green-dark);letter-spacing:.02em}

.headline{left:150px;top:165px;width:549px;height:48px;background:var(--green-dark);border-radius:24px;color:var(--white);font-size:28px;font-weight:900;text-align:center;line-height:48px;letter-spacing:.05em}
.party-art{width:110px;height:90px;border-radius:14px;background:var(--accent-soft)}

.campaign{left:90px;top:228px;width:670px;height:170px}
.early-pill{position:absolute;left:0;top:20px;background:var(--white);color:var(--orange-dark);font-weight:900;font-size:20px;padding:6px 20px;border-radius:20px}
.old-price{position:absolute;left:40px;top:70px;font-size:46px;font-weight:900;color:var(--white);text-decoration:line-through;text-decoration-color:var(--orange-dark)}
.old-price small{font-size:14px}
.arrow{position:absolute;left:320px;top:78px}
.fee-label{position:absolute;left:430px;top:0;font-size:30px;font-weight:900;color:var(--ink)}
.zero{position:absolute;left:430px;top:30px;font-size:128px;line-height:1;font-weight:900;color:var(--orange-dark);-webkit-text-stroke:4px var(--white);paint-order:stroke fill}
.zero small{font-size:56px}

.event{top:420px;width:252px;height:270px;background:var(--white);border-radius:18px;padding:40px 14px 12px;text-align:center}
.month{position:absolute;left:66px;top:-14px;width:120px;height:40px;background:var(--orange);color:var(--white);border-radius:20px;font-size:24px;font-weight:900;line-height:40px}
.month small{font-size:16px}
.event-title{font-size:21px;font-weight:900;color:var(--green-dark);line-height:1.3;min-height:56px;display:flex;align-items:center;justify-content:center}
.event-note{font-size:11px;line-height:1.45;margin:6px 0 8px;font-weight:500}
.date-row{display:flex;align-items:center;gap:6px;justify-content:center;margin-top:6px}
.day{font-size:30px;font-weight:900;color:var(--orange-dark)}
.dow{width:22px;height:22px;border-radius:50%;background:var(--green-dark);color:var(--white);font-size:12px;font-weight:800;line-height:22px}
.venue{font-size:15px;font-weight:800;text-align:left;line-height:1.35}
.gift{width:34px;height:34px;border-radius:8px;background:var(--yellow);flex:none}

.feature{top:712px;width:100px;height:100px;border-radius:50%;background:var(--white);display:flex;align-items:center;justify-content:center;text-align:center;font-size:11px;font-weight:800;line-height:1.35;color:var(--green-dark);padding:8px;border:3px solid var(--yellow)}

.branch{top:868px;width:400px;height:262px;background:var(--white);border-radius:16px;padding:12px 16px}
.branch-name{background:var(--green-dark);color:var(--white);font-size:17px;font-weight:900;border-radius:12px;padding:6px 12px}
.branch-body{display:flex;justify-content:space-between;margin-top:8px}
.branch-info{font-size:12px;font-weight:500;line-height:1.55}
.tel{display:flex;align-items:center;gap:6px;font-size:26px;font-weight:900;color:var(--green-dark);margin-top:4px}
.mail{font-size:13px;font-weight:800;color:var(--ink)}
.photos{display:grid;grid-template-columns:1fr 1fr;gap:8px;margin-top:10px}
.photo{height:78px;border-radius:10px;background:linear-gradient(135deg,var(--photo),#e8e2d6)}
.hours{position:absolute;top:1160px;font-size:12px;font-weight:800;color:var(--white)}
</style>
</head>
<body>
<main class="flyer">

  <header class="masthead abs">
    <p class="tagline">あたま・からだ・こころを育む 学童保育</p>
    <div class="brand"><span class="brand-dot"></span><span class="brand-name">HOSHIZORAキッズ</span></div>
  </header>

  <div class="party-art abs" style="left:24px;top:160px" role="img" aria-label="くす玉と紙吹雪のイラスト"></div>
  <div class="party-art abs" style="left:715px;top:160px" role="img" aria-label="クラッカーと紙吹雪のイラスト"></div>

  <h1 class="headline abs">2024年度 学童入会員 募集スタート！</h1>

  <section class="campaign abs">
    <span class="early-pill">早割キャンペーン</span>
    <p class="old-price">22,000<small>円(税込)</small></p>
    <svg class="arrow" width="90" height="60" viewBox="0 0 90 60"><path d="M0 18h55V0l35 30-35 30V42H0z" fill="#e06a00"/></svg>
    <p class="fee-label">入会金</p>
    <p class="zero">0<small>円</small></p>
  </section>

  <article class="event abs" style="left:28px">
    <div class="month">10<small>月</small></div>
    <h2 class="event-title">学童説明会</h2>
    <div class="date-row"><span class="gift"></span><p class="event-note" style="text-align:left;margin:0">10/28(土)の<br>ハロウィンパーティー<br>招待状をプレゼント</p></div>
    <div class="date-row" style="margin-top:14px"><span class="day">14</span><span class="dow">土</span><p class="venue">さくら台駅前<br>ひかりモール南町</p></div>
  </article>

  <article class="event abs" style="left:298px">
    <div class="month">11<small>月</small></div>
    <h2 class="event-title">秋の体験フェス＆<br>学童体験・説明会</h2>
    <p class="event-note">習いごとの体験イベントを実施！<br>学童の雰囲気を体験できます</p>
    <div class="date-row"><span class="day">11</span><span class="dow">土</span><p class="venue">ひかりモール南町</p></div>
    <div class="date-row"><span class="day">18</span><span class="dow">土</span><p class="venue">さくら台駅前</p></div>
  </article>

  <article class="event abs" style="left:568px">
    <div class="month">12<small>月</small></div>
    <h2 class="event-title">クリスマス会＆<br>学童説明会</h2>
    <p class="event-note">学童入会を検討中の方も<br>クリスマス会にご参加いただけます</p>
    <div class="date-row"><span class="day">9</span><span class="dow">土</span><p class="venue">さくら台駅前</p></div>
    <div class="date-row"><span class="day">16</span><span class="dow">土</span><p class="venue">ひかりモール南町</p></div>
  </article>

  <div class="feature abs" style="left:40px">夜7時まで<br>安心の<br>送迎サポート</div>
  <div class="feature abs" style="left:250px">宿題・学習<br>サポート</div>
  <div class="feature abs" style="left:500px">月1日からの<br>利用も可能</div>
  <div class="feature abs" style="left:710px">STEAM教育を<br>取り入れた<br>カリキュラム</div>

  <section class="branch abs" style="left:16px">
    <h3 class="branch-name">HOSHIZORAキッズ　ひかりモール南町</h3>
    <div class="branch-body">
      <div>
        <p class="branch-info">〒136-0000<br>東京都みどり区南町1-2-3 ひかりモール南町 3F</p>
        <p class="tel"><svg width="24" height="24" viewBox="0 0 24 24"><path d="M6.6 10.8a15 15 0 0 0 6.6 6.6l2.2-2.2c.3-.3.7-.4 1-.2 1.1.4 2.3.6 3.6.6.6 0 1 .4 1 1V20c0 .6-.4 1-1 1A17 17 0 0 1 3 4c0-.6.4-1 1-1h3.5c.6 0 1 .4 1 1 0 1.3.2 2.5.6 3.6.1.3 0 .7-.2 1z" fill="#3f9a36"/></svg>03-5550-0127</p>
        <p class="mail">✉ info@hoshizora-gakudo.jp</p>
      </div>
    </div>
    <div class="photos">
      <div class="photo" role="img" aria-label="教室の写真"></div>
      <div class="photo" role="img" aria-label="学習スペースの写真"></div>
    </div>
  </section>

  <section class="branch abs" style="left:433px">
    <h3 class="branch-name">HOSHIZORAキッズ　さくら台駅前</h3>
    <div class="branch-body">
      <div>
        <p class="branch-info">〒243-0000<br>神奈川県あおば市中町4-5-6 さくら台ビル 2F</p>
        <p class="tel"><svg width="24" height="24" viewBox="0 0 24 24"><path d="M6.6 10.8a15 15 0 0 0 6.6 6.6l2.2-2.2c.3-.3.7-.4 1-.2 1.1.4 2.3.6 3.6.6.6 0 1 .4 1 1V20c0 .6-.4 1-1 1A17 17 0 0 1 3 4c0-.6.4-1 1-1h3.5c.6 0 1 .4 1 1 0 1.3.2 2.5.6 3.6.1.3 0 .7-.2 1z" fill="#3f9a36"/></svg>046-555-0183</p>
        <p class="mail">✉ info@hoshizora-gakudo.jp</p>
      </div>
    </div>
    <div class="photos">
      <div class="photo" role="img" aria-label="教室の写真"></div>
      <div class="photo" role="img" aria-label="遊びスペースの写真"></div>
    </div>
  </section>

  <p class="hours" style="left:24px">営業時間　月〜金 11時〜20時／土曜日9時〜18時</p>
  <p class="hours" style="left:640px">営業時間　月〜金 11時〜20時</p>
</main>
</body>
</html>
```